Keystone Institute Logo & Business card

Keystone Institute - Professional ICT Training
business is a training center.
Logo and business card that have an ID.
bold publicity, distinct, and prestige image
"Ensure professional Success"
that will attract target customer to come and take a look. that will look prestige on certificate after graduation, that will serve as a business tool to attract Business and enterprise customer (let them send their staff for training)

Target Market(s)

young professionals, university students, youth building career in IT fields

Industry/Entity Type

Education

Contact Information for Business Card

Font styles to use
Sans Serif

Colors

Designer to choose colors to be used in the design.

Requirements
Must have
• Logo Identity
• uniqueness
Nice to have
• catch phrase or illustration
Should not have
• just use alphabet as logo.

```html
<!DOCTYPE html>
<html lang="en">
<head>
<meta charset="utf-8">
<title>Keystone Institute – Business Card</title>
<link rel="stylesheet" href="https://fonts.googleapis.com/css2?family=Questrial&family=Roboto:wght@400;700&display=swap">
<style>
  :root {
    --backdrop: #2b2b2d;
    --card: #0c0c0e;
    --card-edge: #1a1a1d;
    --brand-blue: #7fb6ea;
    --violet: #7a3fb0;
    --violet-deep: #4a2f9a;
    --indigo: #3a3a9e;
    --text-light: #8fc3f0;
  }
  * { box-sizing: border-box; margin: 0; padding: 0; }
  html, body {
    width: 1200px; height: 1101px; overflow: hidden;
    background: var(--backdrop);
    font-family: "Roboto", Arial, sans-serif;
  }
  .canvas { position: relative; width: 1200px; height: 1101px; }
  .card {
    position: absolute; left: 170px; width: 860px; height: 491px;
    background: radial-gradient(circle at 60% 45%, #1b1b20 0%, var(--card) 60%);
    border: 1px solid var(--card-edge);
    border-radius: 4px; overflow: hidden;
    box-shadow: 0 18px 40px rgba(0,0,0,.55);
  }
  .card--back { top: 40px; }
  .card--front { top: 570px; }

  .halftone { position: absolute; top: 0; bottom: 0; width: 62%; }
  .card--back .halftone {
    left: 0;
    background: linear-gradient(90deg, rgba(58,58,158,.85) 0%, rgba(122,63,176,.6) 45%, rgba(122,63,176,0) 100%);
  }
  .card--front .halftone {
    right: 0; width: 48%;
    background: linear-gradient(270deg, rgba(58,58,158,.8) 0%, rgba(122,63,176,.55) 45%, rgba(122,63,176,0) 100%);
  }

  .brand { position: absolute; display: flex; align-items: center; gap: 18px; }
  .brand__dot {
    flex: none; border-radius: 50%;
    background: radial-gradient(circle at 35% 30%, #cfe6fb, #5d8fc8 70%, #2c4f86);
  }
  .brand__name {
    font-family: "Questrial", Arial, sans-serif;
    color: var(--brand-blue); white-space: nowrap; line-height: 1;
  }
  .brand__tagline {
    font-family: "Questrial", Arial, sans-serif;
    color: var(--violet); letter-spacing: .22em; text-transform: uppercase;
    margin-top: 8px; white-space: nowrap;
  }

  .card--back .brand { right: 40px; bottom: 60px; }
  .card--back .brand__dot { width: 64px; height: 64px; }
  .card--back .brand__name { font-size: 40px; }
  .card--back .brand__tagline { font-size: 14px; }

  .card--front .brand { left: 50px; top: 50px; }
  .card--front .brand__dot { width: 100px; height: 100px; }
  .card--front .brand__name { font-size: 46px; }
  .card--front .brand__tagline { font-size: 17px; }

  .holder { position: absolute; left: 60px; top: 215px; }
  .holder__name { font-size: 30px; font-weight: 700; color: var(--violet); }
  .holder__role { font-size: 22px; color: var(--text-light); margin-top: 4px; }

  .contacts { position: absolute; left: 60px; top: 318px; list-style: none; }
  .contacts li {
    display: flex; align-items: flex-start; gap: 12px;
    font-size: 20px; color: var(--text-light); line-height: 1.2; margin-bottom: 8px;
  }
  .contacts .icon {
    flex: none; width: 22px; height: 22px; border-radius: 50%;
    background: var(--violet-deep); display: flex; align-items: center; justify-content: center;
  }
  .contacts .icon svg { width: 13px; height: 13px; fill: #0c0c0e; }
</style>
</head>
<body>
<main class="canvas">

  <section class="card card--back" aria-label="Card back">
    <div class="halftone" role="img" aria-label="Violet-to-indigo halftone dot pattern"></div>
    <div class="brand">
      <span class="brand__dot"></span>
      <div>
        <div class="brand__name">Keystone Institute</div>
        <div class="brand__tagline">Professional ICT Training</div>
      </div>
    </div>
  </section>

  <section class="card card--front" aria-label="Card front">
    <div class="halftone" role="img" aria-label="Violet-to-indigo halftone dot pattern"></div>
    <div class="brand">
      <span class="brand__dot"></span>
      <div>
        <div class="brand__name">Keystone Institute</div>
        <div class="brand__tagline">Professional ICT Training</div>
      </div>
    </div>

    <div class="holder">
      <div class="holder__name">Rowan Hale</div>
      <div class="holder__role">Manager</div>
    </div>

    <ul class="contacts">
      <li><span class="icon"><svg viewBox="0 0 24 24"><path d="M6.6 10.8a15 15 0 0 0 6.6 6.6l2.2-2.2a1 1 0 0 1 1-.25 11.4 11.4 0 0 0 3.6.6 1 1 0 0 1 1 1V20a1 1 0 0 1-1 1A17 17 0 0 1 3 4a1 1 0 0 1 1-1h3.5a1 1 0 0 1 1 1c0 1.25.2 2.45.6 3.6a1 1 0 0 1-.25 1z"/></svg></span>0855 12 34 56</li>
      <li><span class="icon"><svg viewBox="0 0 24 24"><path d="M7 2h10a2 2 0 0 1 2 2v16a2 2 0 0 1-2 2H7a2 2 0 0 1-2-2V4a2 2 0 0 1 2-2zm0 3v12h10V5zm5 13.5a1 1 0 1 0 0 2 1 1 0 0 0 0-2z"/></svg></span>info@keystoneinstitute.com</li>
      <li><span class="icon"><svg viewBox="0 0 24 24"><path d="M3 5h18a1 1 0 0 1 1 1v12a1 1 0 0 1-1 1H3a1 1 0 0 1-1-1V6a1 1 0 0 1 1-1zm1 2.5V17h16V7.5l-8 5z M4.5 7 12 11.5 19.5 7z"/></svg></span>www.keystoneinstitute.com</li>
      <li><span class="icon"><svg viewBox="0 0 24 24"><path d="M12 2a7 7 0 0 1 7 7c0 5-7 13-7 13S5 14 5 9a7 7 0 0 1 7-7zm0 4.5a2.5 2.5 0 1 0 0 5 2.5 2.5 0 0 0 0-5z"/></svg></span>No. 2730, cedar lane<br>springfield 418</li>
    </ul>
  </section>

</main>
</body>
</html>
```